Etiketten Fine-Tuning für Creatine Supplement
Zielgruppe
Bitte auf www.kelvora-vital.example hereinschauen.
Please check our webpage: www.kelvora-vital.example
Aufgabenstellung
Eine Vorlage besteht sowie ein Design Guide.
Das bestehende Etikett soll den letzten Feinschliff bekommen um den Kunden optisch zum Kauf anzuregen.
Das Design soll eindeutlich wiedererkennbar sein, große Änderungen sind nicht nötig. Ein minimalistischer Ansatz kann auch gewählt werden.
Weitere Produkte findet ihr auf der Homepage oder auf Zolvex unter dem Begriff Kelvora Vital.
Das Format sollte im Photoshop sein oder irgendwie dort editierbar sein da ich kein Illustrator habe.
Das Etikett muss einen 2 mm Rand für den Zuschnitt haben. Minimale Schriftgrösse ist 1.2mm
Etikettengrösse: 75 x210mm
Die Texte sind verbindlich und müssen verbleiben.
Alle Fonts sind in den Dateien.
A template exists as well as a design guide.
The existing label is to be given the final touches in order to visually encourage the customer to buy.
The design should be clearly recognizable, large changes are not necessary. A minimalist approach can also be chosen.
You can find more products on the homepage or on Zolvex under the term Kelvora Vital.
The format must be in Photoshop. The label must have a 2 mm margin for cutting.
Label size: 75 x210mm
The texts are legally binding and must remain so.

```html
<!DOCTYPE html>
<html lang="de">
<head>
<meta charset="utf-8">
<title>Kelvora Vital Creatine – Etikett</title>
<link rel="stylesheet" href="https://fonts.googleapis.com/css2?family=Montserrat:wght@200;300;800;900&family=Roboto+Condensed:wght@400;700&display=swap">
<style>
  :root {
    --page-bg: #ffffff;
    --label-pale: #eef0da;
    --label-mid: #d6e3b8;
    --label-deep: #bcd89a;
    --circle-green: #93c16f;
    --photo-light: #8a8a8a;
    --photo-dark: #2b2b2b;
    --ink: #1d1d1b;
    --accent-yellow: #f2c500;
    --white: #ffffff;
  }
  * { margin: 0; padding: 0; box-sizing: border-box; }
  html, body {
    width: 1025px;
    height: 1200px;
    overflow: hidden;
    background: var(--page-bg);
  }
  .canvas {
    position: relative;
    width: 1025px;
    height: 1200px;
  }
  .label {
    position: absolute;
    left: 0;
    top: 372px;
    width: 1025px;
    height: 760px;
    overflow: hidden;
    background: linear-gradient(90deg, var(--label-pale) 0%, var(--label-mid) 45%, var(--label-deep) 75%);
  }
  .label-art {
    position: absolute;
    inset: 0;
  }
  .info-column {
    position: absolute;
    left: 40px;
    top: 36px;
    width: 395px;
    font-family: "Roboto Condensed", "Arial Narrow", sans-serif;
    font-size: 17px;
    line-height: 21.5px;
    color: var(--ink);
  }
  .info-block + .info-block { margin-top: 21.5px; }
  .quality-mark {
    position: absolute;
    left: 40px;
    top: 496px;
    font-family: "Montserrat", sans-serif;
  }
  .quality-title {
    font-size: 24px;
    font-weight: 800;
    letter-spacing: 1px;
    color: var(--ink);
  }
  .quality-bar {
    width: 200px;
    height: 6px;
    margin-top: 8px;
    background: var(--accent-yellow);
  }
  .quality-sub {
    margin-top: 6px;
    font-size: 10px;
    font-weight: 800;
    letter-spacing: 1px;
    color: var(--ink);
  }
  .claim {
    position: absolute;
    left: 300px;
    top: 644px;
    width: 175px;
    text-align: center;
    font-family: "Montserrat", sans-serif;
    color: var(--ink);
  }
  .claim-strong {
    font-size: 23px;
    font-weight: 900;
    letter-spacing: 1.5px;
    line-height: 28px;
  }
  .claim-light {
    font-size: 23px;
    font-weight: 300;
    letter-spacing: 1.5px;
    line-height: 30px;
  }
  .claim-web {
    font-family: "Roboto Condensed", sans-serif;
    font-size: 14px;
    font-weight: 700;
    margin-top: 2px;
    white-space: nowrap;
  }
  .product-title {
    position: absolute;
    left: 590px;
    top: 326px;
    width: 380px;
    text-align: center;
    font-family: "Montserrat", sans-serif;
    color: var(--white);
  }
  .product-brand {
    font-size: 44px;
    font-weight: 900;
    letter-spacing: 2px;
    line-height: 52px;
  }
  .product-name {
    font-size: 46px;
    font-weight: 200;
    letter-spacing: 2px;
    line-height: 56px;
  }
</style>
</head>
<body>
<div class="canvas">
  <section class="label">
    <svg class="label-art" width="1025" height="760" viewBox="0 0 1025 760">
      <defs>
        <linearGradient id="photoTop" x1="0" y1="0" x2="1" y2="1">
          <stop offset="0" stop-color="#8a8a8a"/>
          <stop offset="1" stop-color="#2b2b2b"/>
        </linearGradient>
        <linearGradient id="photoBottom" x1="0" y1="0" x2="1" y2="1">
          <stop offset="0" stop-color="#2b2b2b"/>
          <stop offset="1" stop-color="#8a8a8a"/>
        </linearGradient>
        <clipPath id="ringTop"><rect x="0" y="0" width="1025" height="384"/></clipPath>
        <clipPath id="ringBottom"><rect x="0" y="390" width="1025" height="370"/></clipPath>
      </defs>
      <g role="img" aria-label="Schwarz-weiß Fotos: Athlet beim Kreuzheben und Athletin beim Hanteltraining">
        <circle cx="780" cy="380" r="240" fill="url(#photoTop)" clip-path="url(#ringTop)"/>
        <circle cx="780" cy="380" r="240" fill="url(#photoBottom)" clip-path="url(#ringBottom)"/>
      </g>
      <circle cx="780" cy="380" r="190" fill="#93c16f"/>
    </svg>

    <div class="info-column">
      <p class="info-block">Zutaten: Creatin-Monohydrat (99.92% rein), Überzugmittel: Kapselhülle (HPMC, VEGAN), D-Ribose, Alpha-Liponsäure (ALA).<br>Ingredients: Creatine Monohydrate (99.92% rein), Capsule: Capsule shell (HPMC, VEGAN), D-Ribose, Alpha-lipoic acid (ALA).</p>
      <p class="info-block">Die angegebene Tagesdosis sollte nicht überschritten werden. Nahrungsergänzungsmittel sind kein Ersatz für eine ausgewogene, abwechslungsreiche Ernährung und eine gesunde Lebensweise. Außerhalb der Reichweite von Kindern aufbewahren. Nicht geeignet für schwangere und stillende Frauen. Kühl und trocken lagern.</p>
      <p class="info-block">The recommended daily dose should not be exceeded. Supplements should not be used as a substitute of a varied, balanced diet and a healthy lifestyle. Keep out of reach of children. Not suitable for pregnant or nursing women. Store in a cool, dry place.</p>
    </div>

    <div class="quality-mark">
      <p class="quality-title">PREMIUM QUALITÄT</p>
      <div class="quality-bar"></div>
      <p class="quality-sub">PREMIUM QUALITY</p>
    </div>

    <div class="claim">
      <p class="claim-strong">BUILDING A</p>
      <p class="claim-light">BETTER YOU</p>
      <p class="claim-web">www.kelvora-vital.example</p>
    </div>

    <div class="product-title">
      <p class="product-brand">KELVORA</p>
      <p class="product-name">CREATINE</p>
    </div>
  </section>
</div>
</body>
</html>
```